Facebook & Instagram Ads for Quillbright, the world's first device to improve memory throu...

About Us
Quillbright® is a revolutionary bedside device that improves memory while you sleep. Backed by groundbreaking clinical research from the Harlow Ridge Institute of Sciences, our device uses gentle, rotating scents to enhance memory and brian fog naturally. With zero pills, zero side effects, and zero effort, Quillbright offers a new path to better memory. www.quillbright-example.com

The Challenge
We are looking for bold, imaginative, and highly shareable static and GIF ad designs for Facebook and Instagram. This isn’t just another health device—it’s a category-defining product. Your job is to help us stop the scroll with creative ad concepts that communicate the elegance, science, and life-changing benefits of Quillbright.

What We’re Looking For
Format: Static images + short GIF animations (3–8 seconds)
Platforms: Facebook feed, Instagram feed, Instagram Reels
Style: Modern, aspirational, elegant, clean — with a premium feel
Target Audience: Affluent men and women, ages 50+, health-conscious, looking for ways to support memory and brain health and people concerned or worried that they’re losing their memory and aren’t thinking as quickly or crisply as they want,

Creative Direction
Show Quillbright as a premium lifestyle product (not medical or clinical in look).
Think high-end wellness meets cutting-edge science.
Use strong visual hooks: elegant bedside setups, active seniors, subtle cues to scents and sleep, calming colors.
Text overlays should be minimal and impactful.

Tone of Voice (for ad copy in the designs)
Aspirational yet credible
Warm, trustworthy, and empowering
Avoid fear tactics or overpromising

Approved Messaging
✅ Quillbright improves memory while you sleep
✅ Clinically backed & drug-free
✅ Simple, effortless nightly use
✅ No RX, no side effects
✅ Elegant bedside design
✅ Improves your mood
✅ Feel Younger
✅ Developed by a top 2% scientist in the world (Pellington School of Medicine Study)
✅ 226% memory improvement in seniors
✅ 300% memory improvement in dementia patients

Do NOT Say
❌ Cures Alzheimer’s or dementia
❌ Guaranteed results
❌ Any medical claims beyond memory improvement and cognition support

Deliverables
2+ static ad concepts (1080x1080 + 1080x1920 formats)
1+ short GIF ad concepts (3–8 seconds, loopable)
Layered source files (PSD/AI) preferred

What We’ll Provide You
Our website for reference: www.quillbright-example.com
Brand guidelines (logo, colors, fonts)
Approved copy lines and scientific references
Device imagery (with logo placement guidelines)

What We Want to See in Your Work
Unique and scroll-stopping ad ideas (not cookie-cutter templates)
Clever ways to communicate memory improvement + science through visuals
A mix of direct product focus AND lifestyle storytelling

Inspiration
Think of Vartuna, Lumet Band, or Korvel level of sleekness—premium, modern, aspirational.

⚡ Your mission: Help us tell the world about the first device that can improve memory while you sleep—with ads so compelling people can’t scroll past.

```html
<!DOCTYPE html>
<html lang="en">
<head>
<meta charset="utf-8">
<title>Quillbright — Improve Memory While You Sleep</title>
<link href="https://fonts.googleapis.com/css2?family=Bitter:ital,wght@1,800&family=Poppins:wght@300;400&display=swap" rel="stylesheet">
<style>
  :root {
    --ink: #3a2a22;
    --band: #3b2b23;
    --paper: #f4f4f4;
    --paper-edge: #dedede;
    --stage-light: #ececec;
    --stage-dark: #d6d6d6;
    --device-light: #f3f2f0;
    --device-shade: #d9d7d4;
    --bezel: #1c1c1e;
    --frame: #8a8a8e;
    --nav: #f7f7f7;
    --nav-icon: #9a9a9a;
    --white: #ffffff;
  }
  * { margin: 0; padding: 0; box-sizing: border-box; }
  html, body {
    width: 1200px;
    height: 3931px;
    overflow: hidden;
    background: var(--stage-light);
  }

  /* ---------- phone showcase ---------- */
  .showcase {
    position: absolute;
    left: 0;
    top: 0;
    width: 1200px;
    height: 1798px;
    overflow: hidden;
    background: linear-gradient(135deg, var(--stage-dark) 0%, var(--stage-light) 45%, var(--stage-dark) 100%);
  }
  .phone {
    position: absolute;
    width: 472px;
    height: 965px;
    padding: 14px;
    border-radius: 70px;
    background: var(--bezel);
    border: 3px solid var(--frame);
    box-shadow: 30px 30px 60px rgba(0,0,0,0.18);
    transform: rotate(32deg);
  }
  .phone-main { left: 526px; top: 280px; }
  .phone-top { left: 244px; top: -383px; }
  .phone-left { left: -335px; top: 528px; }
  .phone-bottom-left { left: -62px; top: 1257px; }
  .phone-bottom-right { left: 692px; top: 1166px; }
  .phone-screen {
    position: relative;
    width: 100%;
    height: 100%;
    border-radius: 56px;
    overflow: hidden;
    background: var(--paper);
  }
  .status-bar {
    position: absolute;
    left: 0; top: 0;
    width: 100%;
    height: 62px;
    font-family: "Poppins", Arial, sans-serif;
    font-size: 15px;
    color: var(--ink);
  }
  .status-time { position: absolute; left: 60px; top: 22px; }
  .island {
    position: absolute;
    left: 50%;
    top: 16px;
    width: 120px;
    height: 34px;
    margin-left: -60px;
    border-radius: 17px;
    background: var(--bezel);
  }
  .phone-ad {
    position: absolute;
    left: 0;
    top: 62px;
    width: 1200px;
    height: 2133px;
    transform: scale(0.3667);
    transform-origin: top left;
  }
  .nav-bar {
    position: absolute;
    left: 0;
    bottom: 0;
    width: 100%;
    height: 116px;
    background: var(--nav);
    display: flex;
    justify-content: space-around;
    align-items: flex-start;
    padding: 20px 20px 0;
  }
  .nav-bar svg { width: 28px; height: 28px; fill: none; stroke: var(--nav-icon); stroke-width: 2; }
  .nav-bar svg.nav-home { fill: var(--ink); stroke: var(--ink); }

  /* ---------- ad artwork ---------- */
  .ad {
    position: absolute;
    width: 1200px;
    height: 2133px;
    overflow: hidden;
    background: linear-gradient(160deg, var(--paper-edge) 0%, var(--white) 30%, var(--paper) 60%, var(--paper-edge) 100%);
    color: var(--ink);
    font-family: "Poppins", Arial, sans-serif;
  }
  .ad-flat { left: 0; top: 1798px; }
  .brand {
    position: absolute;
    left: 136px;
    top: 96px;
    font-weight: 300;
    font-size: 72px;
    letter-spacing: 4px;
  }
  .headline { font-weight: inherit; }
  .headline-light {
    position: absolute;
    font-weight: 300;
    font-size: 138px;
    line-height: 1;
    letter-spacing: -1px;
  }
  .headline-improve { left: 156px; top: 378px; }
  .headline-memory { left: 290px; top: 502px; }
  .serif-italic {
    font-family: "Bitter", Georgia, serif;
    font-style: italic;
    font-weight: 800;
  }
  .headline-sleep {
    position: absolute;
    left: 164px;
    top: 640px;
    font-size: 101px;
    line-height: 1.1;
    letter-spacing: 8px;
    white-space: nowrap;
  }
  .device-photo {
    position: absolute;
    left: 83px;
    top: 1019px;
    width: 522px;
    height: 980px;
    border-radius: 28px 28px 14px 14px;
    background: linear-gradient(90deg, var(--device-shade) 0%, var(--device-light) 25%, var(--device-light) 70%, var(--device-shade) 100%);
  }
  .claims {
    position: absolute;
    left: 658px;
    top: 1034px;
    width: 530px;
  }
  .claim { margin-bottom: 36px; }
  .claim-lead { font-size: 54px; line-height: 1.1; letter-spacing: 4px; }
  .claim-detail { font-size: 29px; line-height: 1.15; font-weight: 400; }
  .claim-mood { font-size: 41px; letter-spacing: 2px; }
  .cta {
    position: absolute;
    left: 658px;
    top: 1690px;
    font-size: 104px;
    line-height: 1.05;
    letter-spacing: 9px;
  }
  .cta span { display: block; }
  .cta .cta-second { padding-left: 72px; }
  .url-band {
    position: absolute;
    left: 0;
    bottom: 0;
    width: 1200px;
    height: 190px;
    background: var(--band);
    color: var(--white);
    font-weight: 300;
    font-size: 56px;
    text-align: center;
    line-height: 182px;
  }
</style>
</head>
<body>

  <section class="showcase" aria-label="Ad shown on phones">

    <div class="phone phone-top" aria-hidden="true">
      <div class="phone-screen">
        <div class="phone-ad">
          <div class="ad">
            <div class="brand">Quillbright®</div>
            <div class="headline"><span class="headline-light headline-improve">Improve</span><span class="headline-light headline-memory">Memory</span><span class="headline-sleep serif-italic">While You Sleep</span></div>
            <div class="device-photo"></div>
            <div class="claims">
              <div class="claim"><div class="claim-lead serif-italic">Clinically</div><div class="claim-detail">backed &amp; drug-free</div></div>
              <div class="claim"><div class="claim-lead serif-italic">300%</div><div class="claim-detail">memory improvement<br>in dementia patients</div></div>
              <div class="claim"><div class="claim-lead serif-italic">226%</div><div class="claim-detail">memory improvement in seniors</div></div>
              <div class="claim-mood serif-italic">Improves your mood</div>
            </div>
            <div class="cta serif-italic"><span>Order</span><span class="cta-second">Today!</span></div>
            <div class="url-band">www.quillbright-example.com</div>
          </div>
        </div>
        <div class="status-bar"><span class="status-time">22:30</span><span class="island"></span></div>
        <div class="nav-bar">
          <svg class="nav-home" viewBox="0 0 24 24"><path d="M3 11 12 3l9 8v10h-6v-6H9v6H3z"/></svg>
          <svg viewBox="0 0 24 24"><circle cx="10.5" cy="10.5" r="6.5"/><path d="M15.5 15.5 21 21"/></svg>
          <svg viewBox="0 0 24 24"><rect x="3" y="3" width="18" height="18" rx="4"/><path d="M12 8v8M8 12h8"/></svg>
          <svg viewBox="0 0 24 24"><path d="M12 20s-8-5-8-10.5A4.5 4.5 0 0 1 12 7a4.5 4.5 0 0 1 8 2.5C20 15 12 20 12 20z"/></svg>
          <svg viewBox="0 0 24 24"><circle cx="12" cy="8" r="4"/><path d="M4 21c1-4 4-6 8-6s7 2 8 6"/></svg>
        </div>
      </div>
    </div>

    <div class="phone phone-main" aria-hidden="true">
      <div class="phone-screen">
        <div class="phone-ad">
          <div class="ad">
            <div class="brand">Quillbright®</div>
            <div class="headline"><span class="headline-light headline-improve">Improve</span><span class="headline-light headline-memory">Memory</span><span class="headline-sleep serif-italic">While You Sleep</span></div>
            <div class="device-photo"></div>
            <div class="claims">
              <div class="claim"><div class="claim-lead serif-italic">Clinically</div><div class="claim-detail">backed &amp; drug-free</div></div>
              <div class="claim"><div class="claim-lead serif-italic">300%</div><div class="claim-detail">memory improvement<br>in dementia patients</div></div>
              <div class="claim"><div class="claim-lead serif-italic">226%</div><div class="claim-detail">memory improvement in seniors</div></div>
              <div class="claim-mood serif-italic">Improves your mood</div>
            </div>
            <div class="cta serif-italic"><span>Order</span><span class="cta-second">Today!</span></div>
            <div class="url-band">www.quillbright-example.com</div>
          </div>
        </div>
        <div class="status-bar"><span class="status-time">22:30</span><span class="island"></span></div>
        <div class="nav-bar">
          <svg class="nav-home" viewBox="0 0 24 24"><path d="M3 11 12 3l9 8v10h-6v-6H9v6H3z"/></svg>
          <svg viewBox="0 0 24 24"><circle cx="10.5" cy="10.5" r="6.5"/><path d="M15.5 15.5 21 21"/></svg>
          <svg viewBox="0 0 24 24"><rect x="3" y="3" width="18" height="18" rx="4"/><path d="M12 8v8M8 12h8"/></svg>
          <svg viewBox="0 0 24 24"><path d="M12 20s-8-5-8-10.5A4.5 4.5 0 0 1 12 7a4.5 4.5 0 0 1 8 2.5C20 15 12 20 12 20z"/></svg>
          <svg viewBox="0 0 24 24"><circle cx="12" cy="8" r="4"/><path d="M4 21c1-4 4-6 8-6s7 2 8 6"/></svg>
        </div>
      </div>
    </div>

    <div class="phone phone-left" aria-hidden="true">
      <div class="phone-screen">
        <div class="phone-ad">
          <div class="ad">
            <div class="brand">Quillbright®</div>
            <div class="headline"><span class="headline-light headline-improve">Improve</span><span class="headline-light headline-memory">Memory</span><span class="headline-sleep serif-italic">While You Sleep</span></div>
            <div class="device-photo"></div>
            <div class="claims">
              <div class="claim"><div class="claim-lead serif-italic">Clinically</div><div class="claim-detail">backed &amp; drug-free</div></div>
              <div class="claim"><div class="claim-lead serif-italic">300%</div><div class="claim-detail">memory improvement<br>in dementia patients</div></div>
              <div class="claim"><div class="claim-lead serif-italic">226%</div><div class="claim-detail">memory improvement in seniors</div></div>
              <div class="claim-mood serif-italic">Improves your mood</div>
            </div>
            <div class="cta serif-italic"><span>Order</span><span class="cta-second">Today!</span></div>
            <div class="url-band">www.quillbright-example.com</div>
          </div>
        </div>
        <div class="status-bar"><span class="status-time">22:30</span><span class="island"></span></div>
        <div class="nav-bar">
          <svg class="nav-home" viewBox="0 0 24 24"><path d="M3 11 12 3l9 8v10h-6v-6H9v6H3z"/></svg>
          <svg viewBox="0 0 24 24"><circle cx="10.5" cy="10.5" r="6.5"/><path d="M15.5 15.5 21 21"/></svg>
          <svg viewBox="0 0 24 24"><rect x="3" y="3" width="18" height="18" rx="4"/><path d="M12 8v8M8 12h8"/></svg>
          <svg viewBox="0 0 24 24"><path d="M12 20s-8-5-8-10.5A4.5 4.5 0 0 1 12 7a4.5 4.5 0 0 1 8 2.5C20 15 12 20 12 20z"/></svg>
          <svg viewBox="0 0 24 24"><circle cx="12" cy="8" r="4"/><path d="M4 21c1-4 4-6 8-6s7 2 8 6"/></svg>
        </div>
      </div>
    </div>

    <div class="phone phone-bottom-left" aria-hidden="true">
      <div class="phone-screen">
        <div class="phone-ad">
          <div class="ad">
            <div class="brand">Quillbright®</div>
            <div class="headline"><span class="headline-light headline-improve">Improve</span><span class="headline-light headline-memory">Memory</span><span class="headline-sleep serif-italic">While You Sleep</span></div>
            <div class="device-photo"></div>
            <div class="claims">
              <div class="claim"><div class="claim-lead serif-italic">Clinically</div><div class="claim-detail">backed &amp; drug-free</div></div>
              <div class="claim"><div class="claim-lead serif-italic">300%</div><div class="claim-detail">memory improvement<br>in dementia patients</div></div>
              <div class="claim"><div class="claim-lead serif-italic">226%</div><div class="claim-detail">memory improvement in seniors</div></div>
              <div class="claim-mood serif-italic">Improves your mood</div>
            </div>
            <div class="cta serif-italic"><span>Order</span><span class="cta-second">Today!</span></div>
            <div class="url-band">www.quillbright-example.com</div>
          </div>
        </div>
        <div class="status-bar"><span class="status-time">22:30</span><span class="island"></span></div>
        <div class="nav-bar">
          <svg class="nav-home" viewBox="0 0 24 24"><path d="M3 11 12 3l9 8v10h-6v-6H9v6H3z"/></svg>
          <svg viewBox="0 0 24 24"><circle cx="10.5" cy="10.5" r="6.5"/><path d="M15.5 15.5 21 21"/></svg>
          <svg viewBox="0 0 24 24"><rect x="3" y="3" width="18" height="18" rx="4"/><path d="M12 8v8M8 12h8"/></svg>
          <svg viewBox="0 0 24 24"><path d="M12 20s-8-5-8-10.5A4.5 4.5 0 0 1 12 7a4.5 4.5 0 0 1 8 2.5C20 15 12 20 12 20z"/></svg>
          <svg viewBox="0 0 24 24"><circle cx="12" cy="8" r="4"/><path d="M4 21c1-4 4-6 8-6s7 2 8 6"/></svg>
        </div>
      </div>
    </div>

    <div class="phone phone-bottom-right" aria-hidden="true">
      <div class="phone-screen">
        <div class="phone-ad">
          <div class="ad">
            <div class="brand">Quillbright®</div>
            <div class="headline"><span class="headline-light headline-improve">Improve</span><span class="headline-light headline-memory">Memory</span><span class="headline-sleep serif-italic">While You Sleep</span></div>
            <div class="device-photo"></div>
            <div class="claims">
              <div class="claim"><div class="claim-lead serif-italic">Clinically</div><div class="claim-detail">backed &amp; drug-free</div></div>
              <div class="claim"><div class="claim-lead serif-italic">300%</div><div class="claim-detail">memory improvement<br>in dementia patients</div></div>
              <div class="claim"><div class="claim-lead serif-italic">226%</div><div class="claim-detail">memory improvement in seniors</div></div>
              <div class="claim-mood serif-italic">Improves your mood</div>
            </div>
            <div class="cta serif-italic"><span>Order</span><span class="cta-second">Today!</span></div>
            <div class="url-band">www.quillbright-example.com</div>
          </div>
        </div>
        <div class="status-bar"><span class="status-time">22:30</span><span class="island"></span></div>
        <div class="nav-bar">
          <svg class="nav-home" viewBox="0 0 24 24"><path d="M3 11 12 3l9 8v10h-6v-6H9v6H3z"/></svg>
          <svg viewBox="0 0 24 24"><circle cx="10.5" cy="10.5" r="6.5"/><path d="M15.5 15.5 21 21"/></svg>
          <svg viewBox="0 0 24 24"><rect x="3" y="3" width="18" height="18" rx="4"/><path d="M12 8v8M8 12h8"/></svg>
          <svg viewBox="0 0 24 24"><path d="M12 20s-8-5-8-10.5A4.5 4.5 0 0 1 12 7a4.5 4.5 0 0 1 8 2.5C20 15 12 20 12 20z"/></svg>
          <svg viewBox="0 0 24 24"><circle cx="12" cy="8" r="4"/><path d="M4 21c1-4 4-6 8-6s7 2 8 6"/></svg>
        </div>
      </div>
    </div>

  </section>

  <main class="ad ad-flat">
    <div class="brand">Quillbright®</div>

    <h1 class="headline">
      <span class="headline-light headline-improve">Improve</span>
      <span class="headline-light headline-memory">Memory</span>
      <span class="headline-sleep serif-italic">While You Sleep</span>
    </h1>

    <div class="device-photo" role="img" aria-label="Quillbright bedside device: white rounded tower with a copper ring and a front fan grille"></div>

    <div class="claims">
      <div class="claim">
        <div class="claim-lead serif-italic">Clinically</div>
        <div class="claim-detail">backed &amp; drug-free</div>
      </div>
      <div class="claim">
        <div class="claim-lead serif-italic">300%</div>
        <div class="claim-detail">memory improvement<br>in dementia patients</div>
      </div>
      <div class="claim">
        <div class="claim-lead serif-italic">226%</div>
        <div class="claim-detail">memory improvement in seniors</div>
      </div>
      <div class="claim-mood serif-italic">Improves your mood</div>
    </div>

    <div class="cta serif-italic">
      <span>Order</span>
      <span class="cta-second">Today!</span>
    </div>

    <footer class="url-band">www.quillbright-example.com</footer>
  </main>
</body>
</html>
```